Flyer Template Design

I have attached 4 files. I would like a design template that could be used across these documents so that they have a common look and feel. The content of the documents is tested and should not be changed significantly. The images can be changed. I have also attache our logo for color compatibility.
Updates

Need extra days to review

Target Market(s)

Wealthy Christian donors

Font styles to use
Serif
Sans Serif

```html
<!DOCTYPE html>
<html lang="en">
<head>
<meta charset="utf-8">
<title>The Harvest Fund – Flyer</title>
<link href="https://fonts.googleapis.com/css2?family=Roboto:ital,wght@0,400;0,500;0,700;1,400;1,700&display=swap" rel="stylesheet">
<style>
  :root {
    --backdrop: #b9d492;
    --paper: #eceef0;
    --forest: #163d1f;
    --heading: #1b4a24;
    --sky: #6bbde0;
    --ink: #1e1e1e;
    --leaf: #4fa63a;
    --leaf-light: #8fd07a;
  }
  html, body {
    margin: 0;
    width: 1200px;
    height: 1013px;
    overflow: hidden;
    background: var(--backdrop);
    font-family: "Roboto", Arial, sans-serif;
  }
  .flyer {
    position: absolute;
    left: 234px;
    top: 26px;
    width: 636px;
    height: 836px;
    transform: scale(1.15);
    transform-origin: 0 0;
    background: var(--paper);
    overflow: hidden;
    box-shadow: 0 6px 18px rgba(0,0,0,0.18);
    color: var(--ink);
  }
  .flyer-shapes { position: absolute; inset: 0; }
  .photo {
    position: absolute;
    border-radius: 50%;
    border: 4px solid #fff;
    box-sizing: border-box;
  }
  .photo--elder {
    left: 266px; top: 37px; width: 156px; height: 156px;
    background: radial-gradient(circle at 45% 40%, #d6d6d6, #7d7d7d 60%, #3a3a3a);
  }
  .photo--children {
    left: 398px; top: 130px; width: 206px; height: 206px;
    background: radial-gradient(circle at 50% 40%, #b07a5a, #7a2a3a 55%, #3a1420);
  }
  .brand {
    position: absolute;
    left: 428px; top: 20px;
    display: flex; align-items: center; gap: 12px;
  }
  .brand-mark {
    width: 44px; height: 44px;
    background: var(--heading);
  }
  .brand-name {
    font-size: 17px;
    line-height: 18px;
    font-weight: 400;
    color: var(--heading);
    letter-spacing: 0.3px;
  }
  .section { position: absolute; }
  .section h2 {
    margin: 0 0 6px;
    font-size: 19px;
    line-height: 22px;
    font-weight: 700;
    font-style: italic;
    color: var(--heading);
  }
  .section p {
    margin: 0;
    font-size: 10.6px;
    line-height: 14px;
    text-align: justify;
  }
  .section--commission { left: 37px; top: 178px; width: 274px; }
  .section--nations { left: 37px; top: 355px; width: 274px; }
  .section--stand { left: 340px; top: 355px; width: 258px; }
  .section--coming { left: 340px; top: 530px; width: 258px; }
  .section--commission h2 { margin-left: 2px; }
  .callout {
    position: absolute;
    left: 37px; top: 552px; width: 274px;
    margin: 0;
    text-align: center;
    font-size: 25px;
    line-height: 27px;
    font-weight: 700;
    color: var(--heading);
  }
  .appeal {
    position: absolute;
    left: 37px; top: 680px; width: 560px;
    text-align: center;
  }
  .appeal h3 {
    margin: 0 0 4px;
    font-size: 14px;
    font-weight: 700;
    font-style: italic;
  }
  .appeal p {
    margin: 0;
    font-size: 10.6px;
    line-height: 14px;
    text-align: justify;
    text-align-last: center;
  }
  .cta {
    position: absolute;
    left: 20px; top: 770px; width: 596px;
    margin: 0;
    text-align: center;
    font-size: 15px;
    line-height: 21px;
    font-weight: 500;
    color: var(--forest);
  }
  .cta em { font-size: 17.5px; font-weight: 500; }
  .footer-band {
    position: absolute;
    left: 0; bottom: 0; width: 636px; height: 13px;
    background: linear-gradient(90deg, var(--leaf), var(--leaf-light));
  }
</style>
</head>
<body>
  <div class="flyer">
    <svg class="flyer-shapes" width="636" height="836" viewBox="0 0 636 836" aria-hidden="true">
      <path fill="var(--forest)" d="M0,0 H636 V440 C600,380 520,250 430,130 C330,62 150,30 0,45 Z"/>
      <path fill="var(--sky)" d="M0,45 C150,30 250,42 300,70 L296,98 C200,78 90,82 0,112 Z"/>
      <path fill="var(--sky)" d="M566,320 C590,360 615,400 636,432 L636,446 C610,410 585,375 556,338 Z"/>
      <circle cx="515" cy="-2" r="115" fill="#f2f2f2"/>
    </svg>

    <div class="photo photo--elder" role="img" aria-label="Black and white portrait of an elderly woman"></div>
    <div class="photo photo--children" role="img" aria-label="Photo of young girls in colourful traditional dress"></div>

    <div class="brand">
      <div class="brand-mark"></div>
      <div class="brand-name">THE<br>HARVEST<br>FUND</div>
    </div>

    <section class="section section--commission">
      <h2>FINISHING<br>THE GREAT COMMISSION</h2>
      <p>Before Jesus ascended into heaven, He commanded his apostles, <em><strong>“Go and make disciples of all nations.”</strong></em> For more than 2000 years the church has been working to fulfill this <em>“Great Commission,”</em> and much has been accomplished. But now, for the first time in history, our generation has the real opportunity to finish the Great Commission in our lifetimes.</p>
    </section>

    <section class="section section--nations">
      <h2>IT’S ABOUT NATIONS</h2>
      <p>In the Bible, the word <em><strong>“nations”</strong></em> refers to people groups: <em><strong>groups of people who share a common ethnicity, culture, and language.</strong></em><br>So when Jesus said, <em><strong>“Go and make disciples if all nations,”</strong></em> He was telling us to take the gospel to every people group on earth.<br>Amazingly, there are about 12,000 of these people groups scattered throughout the world. And the Great Commission commands us to make disciples in every one of them.</p>
    </section>

    <section class="section section--stand">
      <h2>WHERE DO WE STAND?</h2>
      <p>Today, there are still about 500 people groups who have never heard the gospel. Most of these groups are small and located in remote, difficult places. These remaining <em><strong>“unengaged”</strong></em> people groups have no known believers.<br>But now that we know who and where these groups are, by God’s grace it is possible that we can engage every one of them with the gospel within the next 3 years.</p>
    </section>

    <section class="section section--coming">
      <h2>HESTENING HIS COMING</h2>
      <p>The Bible says that believers <em><strong>“ought to live holy and godly lives, looking for and hastening the coming of the day of God.”</strong></em> It also says that day will not come until the gospel has been preached to <em>“all nations.”</em> So how can hasten the day of his coming? By finishing the work he gave us to do: <em><strong>making disciples in all nations</strong></em>.</p>
    </section>

    <p class="callout">In other words,we<br>can finish the<br>Great Commission!</p>

    <div class="appeal">
      <h3>You can make that happen.</h3>
      <p>Partner with the Harvest Fund and finance the missionaries who are taking the gospel for the first time to those last remaining people groups. Your investment will “<em><strong>hasten the coming of the day of God</strong></em>” by accelerating the effort to make “<em><strong>disciples in every nation.”</strong></em> In 2018, our partners helped take the gospel to 231 people groups in 35 countries.</p>
    </div>

    <p class="cta"><em>JOIN US</em> as we invest to make disciples in <em>“all nations”</em> by 2022.<br><em>To learn more</em>, Email Daniel Marsh at <em>dmarsh@harvestfund.org</em>.</p>

    <div class="footer-band"></div>
  </div>
</body>
</html>
```